Etikett für ein Erfrischungsgetränk
Zielgruppe
Veltrano ist ein Startup Unternehmen, welches in naher Zukunft ein
Hibiskus-Erfrischungsgetränk auf den Markt bringen möchte.
Die Zielgruppe ist jedermann. Ob jung oder alt.
Aufgabenstellung
Das Etikett einer 0,33 l Longneckflasche soll:
Erfrischend, Modern aber auch Zeitlos, Einzigartig, dezent wirken.
Das Logo soll hervorstehen und der Hintergrund dezent sein.
Vorderetikett: 76 mm breit, 86 mm hoch
Rücketikett: 55 mm breit, 75 mm hoch
Die Getränkfarbe ist rötlich.

```html
<!DOCTYPE html>
<html lang="de">
<head>
<meta charset="utf-8">
<title>Veltrano – Vorderetikett</title>
<link rel="stylesheet" href="https://fonts.googleapis.com/css2?family=Arimo:wght@400;700&display=swap">
<style>
  :root {
    --page: #f4f4f2;
    --aqua: #43c6e8;
    --aqua-light: #9fe2f2;
    --leaf: #8fd08c;
    --lime: #dbe68c;
    --magenta: #de1a83;
    --berry: #8e1e6e;
    --white: #ffffff;
    --flower: #e6485e;
  }
  * { margin: 0; padding: 0; box-sizing: border-box; }
  html, body {
    width: 1200px;
    height: 3723px;
    overflow: hidden;
    background: var(--page);
    font-family: "Arimo", Arial, sans-serif;
  }
  .canvas {
    position: relative;
    width: 1200px;
    height: 3723px;
  }
  /* Vorderetikett 76 × 86 mm */
  .label {
    position: absolute;
    left: 100px;
    top: 1295px;
    width: 1000px;
    height: 1132px;
    overflow: hidden;
  }
  .label-background {
    position: absolute;
    inset: 0;
    background:
      radial-gradient(ellipse 320px 240px at 22% 30%, var(--aqua-light) 0%, transparent 70%),
      radial-gradient(ellipse 260px 200px at 82% 40%, rgba(255,255,255,0.35) 0%, transparent 70%),
      radial-gradient(ellipse 380px 260px at 80% 78%, var(--leaf) 0%, transparent 70%),
      linear-gradient(180deg, var(--aqua) 0%, var(--aqua) 48%, var(--leaf) 76%, var(--lime) 100%);
  }
  .brand {
    position: absolute;
    top: 50px;
    left: 0;
    right: 0;
    display: flex;
    align-items: center;
    justify-content: center;
    gap: 26px;
  }
  .brand-name {
    font-weight: 700;
    font-size: 170px;
    line-height: 1;
    color: var(--berry);
  }
  .brand-dot {
    width: 48px;
    height: 48px;
    border-radius: 50%;
    background: var(--magenta);
  }
  .drink-illustration {
    position: absolute;
    left: 270px;
    top: 300px;
    width: 440px;
    height: 560px;
    background:
      radial-gradient(circle 105px at 72% 18%, var(--flower) 0%, var(--flower) 80%, transparent 100%),
      linear-gradient(172deg, rgba(255,255,255,0.55) 0%, rgba(255,255,255,0.3) 60%, rgba(255,255,255,0.18) 100%);
    border-radius: 30px 30px 60px 60px;
  }
  .claim {
    position: absolute;
    left: 170px;
    top: 855px;
    width: 660px;
    height: 170px;
    border-radius: 85px;
    background: var(--magenta);
    color: var(--white);
    text-align: center;
    padding-top: 30px;
  }
  .claim-title {
    font-size: 60px;
    font-weight: 400;
    line-height: 1.1;
  }
  .claim-sub {
    margin-top: 10px;
    font-size: 38px;
    font-weight: 400;
    line-height: 1.1;
  }
</style>
</head>
<body>
  <main class="canvas">
    <section class="label">
      <div class="label-background" role="img" aria-label="Aquarellhintergrund in Türkis, Grün und Gelb mit zarten weißen Wirbeln"></div>

      <div class="brand">
        <span class="brand-name">Veltrano</span>
        <span class="brand-dot"></span>
      </div>

      <div class="drink-illustration" role="img" aria-label="Weiße Kreidezeichnung eines hohen Glases mit sprudelndem Getränk, am Rand eine rote Hibiskusblüte"></div>

      <div class="claim">
        <p class="claim-title">Erfrischungsgetränk</p>
        <p class="claim-sub">aus aufgebrühtem Hibiskustee</p>
      </div>
    </section>
  </main>
</body>
</html>
```